Yoga Studio Postcard Advertising Flyer

Need a postcard size flyer that will promote our business. The objective is to promote location and availability. Want it to be personal. The objective to connect the audience to the purpose of yoga and the focus on enabling functional well-being. Something that is a very big focus at this point in time in the world. I really want people to see the value in connecting with us via our website, calmora app, pagewell or vibro. The colours are to be bright but not overwhelming and aligned to the logo colours. Its also important to have the location picture on the flyer - unless you think that it is way too much (try a with or without). I don't want this to be a specials brochure - it is an introduction to our brand and our business. No need to over do it with promotional lines apart from come and join us.

Delayed in organising this.

Local yogis and residence who are or want to be focused on well-being.

• Pictures - would have the logo on one side.
• Modern and aligned to website design.

```html
<!DOCTYPE html>
<html lang="en">
<head>
<meta charset="utf-8">
<title>Azure Petal Yoga – Enable Functional Wellbeing</title>
<link rel="stylesheet" href="https://fonts.googleapis.com/css2?family=Montserrat:wght@200;300;700&family=Montserrat+Alternates:wght@400&display=swap">
<style>
  :root {
    --sky-top: #cfeaf3;
    --sky-low: #e4f4f7;
    --horizon: #c7e9ec;
    --sea: #8fd2d4;
    --sea-deep: #6dbfc4;
    --brand-blue: #2aa5df;
    --panel-navy: #0b1a36;
    --white: #ffffff;
  }
  * { box-sizing: border-box; margin: 0; padding: 0; }
  html, body { width: 1200px; height: 846px; overflow: hidden; }
  body { background: var(--white); }

  .postcard {
    position: relative;
    width: 1200px;
    height: 846px;
    overflow: hidden;
  }

  .scene {
    position: absolute;
    inset: 0;
    background: linear-gradient(180deg,
      var(--sky-top) 0%,
      var(--sky-low) 45%,
      var(--horizon) 61%,
      var(--sea) 72%,
      var(--sea-deep) 100%);
  }

  .headline {
    position: absolute;
    right: 128px;
    top: 72px;
    text-align: right;
    color: var(--brand-blue);
    font-family: "Montserrat", sans-serif;
  }
  .headline__lead {
    display: block;
    font-weight: 200;
    font-size: 62px;
    line-height: 66px;
  }
  .headline__main {
    display: block;
    font-weight: 700;
    font-size: 63px;
    line-height: 70px;
    letter-spacing: -0.5px;
  }

  .info-panel {
    position: absolute;
    left: 758px;
    top: 240px;
    width: 341px;
    height: 606px;
    background: var(--panel-navy);
  }

  .values {
    position: absolute;
    right: 16px;
    top: 34px;
    text-align: right;
    font-family: "Montserrat Alternates", sans-serif;
    font-weight: 400;
    font-size: 20.5px;
    line-height: 24.5px;
    color: var(--brand-blue);
  }
  .values p + p { margin-top: 24px; }

  .brand {
    position: absolute;
    left: 0;
    right: 0;
    top: 440px;
    display: flex;
    flex-direction: column;
    align-items: center;
    gap: 16px;
  }
  .brand__dot {
    width: 44px;
    height: 44px;
    border-radius: 50%;
    background: var(--brand-blue);
  }
  .brand__name {
    font-family: "Montserrat Alternates", sans-serif;
    font-weight: 400;
    font-size: 22px;
    letter-spacing: 1px;
    color: var(--white);
    text-align: center;
    line-height: 30px;
  }
</style>
</head>
<body>
  <main class="postcard">
    <div class="scene" role="img" aria-label="Photo of a woman in white sitting cross-legged in a yoga pose with palms joined overhead at the end of a wooden pier, looking out over a calm turquoise sea under a bright hazy sky"></div>

    <h1 class="headline">
      <span class="headline__lead">Enable</span>
      <span class="headline__main">Functional Wellbeing</span>
    </h1>

    <section class="info-panel">
      <div class="values">
        <p>Strengthen<br>your well-being through<br>adaptive yoga.</p>
        <p>Seek to evolve<br>your mind and body through<br>the challenge of yoga.</p>
        <p>Perfection is a desire and<br>never an outcome through<br>the practice of yoga.</p>
      </div>

      <div class="brand">
        <span class="brand__dot" aria-hidden="true"></span>
        <span class="brand__name">AZURE PETAL YOGA</span>
      </div>
    </section>
  </main>
</body>
</html>
```